Tervolan Pty Ltd professional business card

A professional business card template using the colours from the supplied logo.
Clean crisp lines while, Modern while not being over the top.

Target Market(s)

Construction, commerical and industrial

Industry/Entity Type

Communications

Contact Information for Business Card

For a Communications, IT, Optical fibre installation company

Colors
37b8a4

```html
<!DOCTYPE html>
<html lang="en">
<head>
<meta charset="utf-8">
<title>Tervolan Pty Ltd – Business Card</title>
<link rel="stylesheet" href="https://fonts.googleapis.com/css2?family=Poppins:wght@300;400;500;700&display=swap">
<style>
  :root {
    --page-bg: #2b2b2d;
    --card-grey: #6a6a6c;
    --card-white: #ffffff;
    --wordmark-grey: #6d6e71;
    --teal: #37b8a4;
    --text-light: #ffffff;
  }
  * { box-sizing: border-box; margin: 0; padding: 0; }
  html, body {
    width: 1200px; height: 900px; overflow: hidden;
    background: var(--page-bg);
    font-family: "Poppins", sans-serif;
  }
  .stage {
    width: 1200px; height: 900px;
    display: flex; flex-direction: column;
    align-items: center; justify-content: center; gap: 40px;
  }
  .card {
    width: 700px; height: 400px;
    position: relative; overflow: hidden;
    box-shadow: 0 10px 30px rgba(0,0,0,0.45);
  }
  /* Back */
  .card-back {
    background: var(--card-grey);
    display: flex; flex-direction: column;
    align-items: center; justify-content: center;
  }
  .wordmark {
    font-weight: 500; letter-spacing: 2px; line-height: 1;
  }
  .card-back .wordmark { color: var(--text-light); font-size: 64px; }
  .card-back .web {
    margin-top: 70px; color: var(--text-light);
    font-size: 15px; font-weight: 500; letter-spacing: 5px;
  }
  /* Front */
  .card-front { display: flex; }
  .front-info {
    width: 48%; background: var(--card-grey);
    padding: 44px 0 0 46px; color: var(--text-light);
  }
  .person-name { font-size: 24px; line-height: 1.1; letter-spacing: 0.5px; }
  .person-name .first { font-weight: 700; }
  .person-name .last { font-weight: 300; }
  .person-role { color: var(--teal); font-size: 18px; font-weight: 400; }
  .contact-group {
    display: flex; align-items: center; gap: 14px;
    margin-top: 62px;
  }
  .contact-group + .contact-group { margin-top: 22px; }
  .contact-icons {
    display: flex; flex-direction: column; gap: 8px; width: 18px;
    align-items: center;
  }
  .contact-icons svg { width: 16px; height: 16px; }
  .divider { width: 2px; align-self: stretch; background: var(--teal); }
  .contact-lines { font-size: 16px; font-weight: 500; line-height: 1.4; }
  .front-brand {
    flex: 1; background: var(--card-white);
    display: flex; align-items: center; justify-content: center;
  }
  .front-brand .wordmark { color: var(--wordmark-grey); font-size: 50px; }
</style>
</head>
<body>
<main class="stage">
  <section class="card card-back">
    <div class="wordmark">TERVOLAN</div>
    <div class="web">WWW.TERVOLAN.COM.AU</div>
  </section>

  <section class="card card-front">
    <div class="front-info">
      <h1 class="person-name"><span class="first">DANIEL</span> <span class="last">REYES</span></h1>
      <p class="person-role">CEO/Founder</p>

      <div class="contact-group">
        <div class="contact-icons">
          <svg viewBox="0 0 24 24" aria-hidden="true"><path fill="#37b8a4" d="M6.6 10.8a15 15 0 006.6 6.6l2.2-2.2a1 1 0 011-.25 11.4 11.4 0 003.6.57 1 1 0 011 1V20a1 1 0 01-1 1A17 17 0 013 4a1 1 0 011-1h3.5a1 1 0 011 1c0 1.25.2 2.45.57 3.6a1 1 0 01-.25 1z"/></svg>
          <svg viewBox="0 0 24 24" aria-hidden="true"><rect x="2" y="5" width="20" height="14" fill="none" stroke="#37b8a4" stroke-width="2"/><path d="M2 5l10 8 10-8" fill="none" stroke="#37b8a4" stroke-width="2"/></svg>
          <svg viewBox="0 0 24 24" aria-hidden="true"><g fill="none" stroke="#37b8a4" stroke-width="1.8"><circle cx="12" cy="12" r="10"/><ellipse cx="12" cy="12" rx="4.5" ry="10"/><path d="M2 12h20M4 7h16M4 17h16"/></g></svg>
        </div>
        <div class="divider"></div>
        <div class="contact-lines">
          <div>555-014-2290</div>
          <div>daniel@tervolan.com.au</div>
          <div>www.tervolan.com.au</div>
        </div>
      </div>

      <div class="contact-group">
        <div class="contact-icons">
          <svg viewBox="0 0 24 24" aria-hidden="true"><path fill="#37b8a4" d="M12 2a7 7 0 00-7 7c0 5 7 13 7 13s7-8 7-13a7 7 0 00-7-7zm0 9.5A2.5 2.5 0 1112 6.5a2.5 2.5 0 010 5z"/></svg>
        </div>
        <div class="divider"></div>
        <div class="contact-lines">
          <div>118 Harlow Street NW</div>
          <div>Suite 210, Eastbrook</div>
          <div>MI 40112</div>
        </div>
      </div>
    </div>
    <div class="front-brand">
      <div class="wordmark">TERVOLAN</div>
    </div>
  </section>
</main>
</body>
</html>
```